infographic about brain health and home health

We want one side to be about brain health and have our logo as well as the logo for Velmora Wellness Center, and then on the other side, all about home health care .... with our logo and our contact information.

```html
<!DOCTYPE html>
<html lang="en">
<head>
<meta charset="utf-8">
<title>Solenne Healthcare – Home Care &amp; Brain Health Flyers</title>
<link rel="stylesheet" href="https://fonts.googleapis.com/css2?family=Roboto:ital,wght@0,400;0,500;0,700;0,900;1,400&family=Great+Vibes&family=Sacramento&display=swap">
<style>
:root{
  --teal:#5ec4cf;
  --teal-dark:#2fa3b1;
  --teal-light:#d3f0f3;
  --ink:#1b1b1b;
  --white:#ffffff;
  --stage:#a7a7ab;
  --sans:'Roboto', Arial, sans-serif;
  --script:'Great Vibes', cursive;
  --script-thin:'Sacramento', cursive;
}
*{box-sizing:border-box;margin:0;padding:0}
html,body{width:1200px;height:1200px;overflow:hidden}
body{background:var(--stage);font-family:var(--sans);color:var(--ink);position:relative}
.flyer{position:absolute;top:240px;width:520px;height:738px;background:var(--white);overflow:hidden}
.flyer--home{left:62px}
.flyer--brain{left:620px;background:linear-gradient(180deg,#ffffff 0%,var(--teal-light) 35%,#c2e9ee 100%)}
.abs{position:absolute}

/* ---------- home care ---------- */
.hero-photo{left:0;top:0;width:520px;height:290px;background:linear-gradient(135deg,#6d7a3c 0%,#a89a66 40%,#c4a98a 65%,#5f6a38 100%)}
.brand-corner{left:0;top:0;width:205px;height:128px;background:var(--ink);border-bottom-right-radius:95px;border-bottom:5px solid var(--teal);border-right:5px solid var(--teal)}
.brand-name{position:absolute;left:18px;top:56px;width:170px;text-align:center;color:var(--white);font-weight:400;font-size:15px;letter-spacing:7px}
.brand-sub{position:absolute;left:18px;top:78px;width:170px;text-align:center;color:var(--white);font-size:6px;letter-spacing:4px}
.hero-title{left:34px;top:218px;font-family:var(--script);font-size:58px;color:var(--ink);text-shadow:0 0 6px #fff}
.intro-band{left:0;top:289px;width:520px;height:56px;background:var(--teal);padding:8px 22px;text-align:center;font-size:9.6px;line-height:12.5px;color:var(--ink)}
.who{left:10px;top:360px;width:220px;text-align:center}
.who-script{font-family:var(--script-thin);color:var(--teal);font-size:34px;line-height:34px}
.who-head{font-size:14px;font-weight:500;margin-top:-2px}
.who-rule{width:150px;height:2px;background:var(--teal);margin:4px auto 10px}
.who-list{font-size:11.5px;line-height:15.5px}
.who-list .lead{font-size:14px;font-weight:500;line-height:17px}
.who-list b{color:var(--teal-dark);font-weight:500}
.who-art{left:22px;top:515px;width:195px;height:130px;background:radial-gradient(ellipse at center,#9fdde4 0%,#dff4f6 70%,#fff 100%);border-radius:8px}
.benefits{left:238px;top:358px;width:270px;height:300px;background:var(--ink);border:3px solid var(--teal);border-radius:18px;color:var(--white);text-align:center}
.benefits-script{font-family:var(--script-thin);color:var(--teal);font-size:32px;line-height:30px;margin-top:6px}
.benefits-head{font-size:13px;font-weight:500;letter-spacing:.3px}
.benefit-grid{position:absolute;left:10px;top:72px;width:246px;height:218px;display:grid;grid-template-columns:1fr 1fr;grid-template-rows:1fr 1fr 1fr}
.benefit{display:flex;flex-direction:column;align-items:center;justify-content:flex-end;padding-bottom:8px;font-size:7.8px;line-height:9px;font-weight:500}
.benefit svg{margin-bottom:8px}
.benefit:nth-child(odd){border-right:2px dotted var(--teal)}
.benefit:nth-child(-n+4){border-bottom:2px dotted var(--teal)}
.footer{left:0;top:676px;width:520px;height:62px;background:var(--ink)}
.footer-swoosh{position:absolute;right:0;top:-14px}
.footer-phone{position:absolute;left:22px;top:18px;display:flex;align-items:center;gap:10px;color:var(--white);font-size:20px;font-weight:700}
.footer-contact{position:absolute;right:14px;top:8px;text-align:right;color:var(--ink)}
.footer-email{font-size:11px;display:flex;justify-content:flex-end;align-items:center;gap:5px}
.footer-web{font-size:19px;font-weight:700;display:flex;justify-content:flex-end;align-items:center;gap:5px}
.dot{display:inline-block;width:10px;height:10px;border-radius:50%;background:var(--ink)}

/* ---------- brain health ---------- */
.call-bar{left:188px;top:0;width:332px;height:42px;background:var(--ink);color:var(--white);display:flex;align-items:center;justify-content:flex-end;gap:10px;padding-right:16px}
.call-script{font-family:var(--script-thin);font-size:28px}
.call-num{font-size:19px;font-weight:700}
.info-band{left:0;top:42px;width:520px;height:82px;background:var(--teal);padding:3px 14px 0 200px;text-align:right;font-size:8.9px;line-height:12px;color:var(--ink)}
.partner-corner{left:0;top:0;width:200px;height:128px;background:var(--white);border-bottom-right-radius:110px;border-bottom:5px solid var(--teal);border-right:5px solid var(--teal)}
.partner-mark{position:absolute;left:14px;top:26px;width:40px;height:40px;border-radius:50%;border:4px solid #9a9a9a}
.partner-name{position:absolute;left:62px;top:32px;width:120px;font-size:10.5px;font-weight:500;line-height:13px;color:var(--ink)}
.brain-badge{width:100px;height:100px;border-radius:50%;background:var(--teal);display:flex;align-items:center;justify-content:center}
.brain-badge span{width:82px;height:82px;border-radius:50%;background:var(--ink);display:block}
.badge-left{left:68px;top:137px}
.badge-right{left:332px;top:133px}
.brain-title{left:180px;top:142px;width:160px;text-align:center;font-family:var(--script-thin);font-size:32px;line-height:30px;color:var(--teal-dark)}
.brain-title em{font-style:normal;color:var(--ink)}
.arrows{left:0;top:0}
.list-title{font-size:19px;font-weight:900;line-height:19px;text-align:center}
.boosters-title{left:40px;top:262px;width:175px;color:var(--ink)}
.busters-title{left:295px;top:258px;width:180px;color:var(--teal)}
.food-list{list-style:none}
.food-list li{display:flex;gap:8px;align-items:flex-start}
.food-list i{flex:none;width:20px;height:20px;border:2px solid currentColor;border-radius:50%;margin-top:1px}
.food-list strong{display:block;font-size:7.8px;font-weight:700;line-height:9px}
.food-list span{display:block;font-size:6.6px;font-style:italic;line-height:8px}
.boosters{left:46px;top:322px;width:168px;color:var(--ink)}
.boosters li{height:32px}
.busters{left:300px;top:322px;width:172px;color:var(--white)}
.busters li{height:27px}
.busters i{border-color:var(--teal)}
.footer-brand{position:absolute;left:70px;top:12px;width:110px;text-align:center;color:var(--white)}
.footer-brand .n{font-size:10px;letter-spacing:5px}
.footer-brand .s{font-size:5px;letter-spacing:3px;margin-top:2px}
</style>
</head>
<body>

<!-- Home care flyer -->
<section class="flyer flyer--home">
  <div class="abs hero-photo" role="img" aria-label="Photo of a smiling caregiver with an older man in a wheelchair outdoors in a garden"></div>
  <div class="abs brand-corner">
    <div class="brand-name">SOLENNE</div>
    <div class="brand-sub">HEALTHCARE</div>
  </div>
  <h1 class="abs hero-title">Home Care</h1>
  <p class="abs intro-band">We focus on helping people to thrive and function in their own homes regardless of age or health challenges. Above all, Solenne Healthcare empowers people to maintain an independent lifestyle in the community and successfully age in place.</p>

  <div class="abs who">
    <div class="who-script">Who is</div>
    <div class="who-head">RECEIVING HOMECARE?</div>
    <div class="who-rule"></div>
    <div class="who-list">
      <div class="lead">PEOPLE</div>
      <div><b>MANAGING</b> Chronic Conditions</div>
      <div><b>RECOVERING</b> from Acute Illness</div>
      <div>with <b>DEMENTIA</b></div>
      <div>plus <b>OLDER ADULTS</b></div>
    </div>
  </div>
  <div class="abs who-art" role="img" aria-label="Teal pictograms of patients, caregivers and caring hands"></div>

  <div class="abs benefits">
    <div class="benefits-script">Benefits</div>
    <div class="benefits-head">OF SOLENNE HOMECARE</div>
    <div class="benefit-grid">
      <div class="benefit">
        <svg width="44" height="30" viewBox="0 0 44 30"><path d="M4 4h8v10h6L8 26-2 14h6z" fill="#fff" transform="translate(2 0)"/><rect x="22" y="7" width="18" height="14" rx="3" fill="#fff" transform="rotate(-35 31 14)"/></svg>
        LOWER COSTS</div>
      <div class="benefit">
        <svg width="26" height="32" viewBox="0 0 26 32"><rect x="4" y="10" width="18" height="20" rx="4" fill="#fff"/><path d="M13 0v7M5 3l3 5M21 3l-3 5" stroke="#5ec4cf" stroke-width="2"/></svg>
        PRESERVES AUTONOMY</div>
      <div class="benefit">
        <svg width="50" height="30" viewBox="0 0 50 30"><g fill="#fff"><circle cx="10" cy="8" r="4"/><circle cx="25" cy="5" r="4"/><circle cx="40" cy="8" r="4"/><rect x="6" y="13" width="8" height="15" rx="2"/><rect x="21" y="10" width="8" height="18" rx="2"/><rect x="36" y="13" width="8" height="15" rx="2"/></g></svg>
        PRESERVES SOCIAL TIES</div>
      <div class="benefit">
        <svg width="34" height="30" viewBox="0 0 34 30"><circle cx="13" cy="7" r="6" fill="#fff"/><path d="M1 29c0-9 6-13 12-13s12 4 12 13z" fill="#fff"/><path d="M27 12v12M21 18h12" stroke="#5ec4cf" stroke-width="3"/></svg>
        ENCOURAGES<br>PATIENT CENTEREDNESS</div>
      <div class="benefit">
        <svg width="48" height="30" viewBox="0 0 48 30"><path d="M4 2h8v12h6L8 28-2 14h6z" fill="#fff" transform="translate(2 0)"/><path d="M34 2l13 26H21z" fill="#fff"/><rect x="33" y="10" width="2.5" height="10" fill="#1b1b1b"/><rect x="33" y="22" width="2.5" height="2.5" fill="#1b1b1b"/></svg>
        REDUCES RISK<br>SOME COMPLICATIONS</div>
      <div class="benefit">
        <svg width="30" height="30" viewBox="0 0 30 30"><circle cx="12" cy="12" r="9" fill="none" stroke="#fff" stroke-width="3"/><path d="M19 19l9 9" stroke="#fff" stroke-width="4"/></svg>
        ALLOWS FOR ASSESSMENT<br>OF SOCIAL DETERMINANTS<br>OF HEALTH</div>
    </div>
  </div>

  <footer class="abs footer">
    <svg class="footer-swoosh" width="300" height="76" viewBox="0 0 300 76"><path d="M0 76C80 30 170 8 300 0v76z" fill="#5ec4cf"/><path d="M40 76C110 42 190 26 300 22v54z" fill="#5ec4cf"/></svg>
    <div class="footer-phone">
      <svg width="26" height="26" viewBox="0 0 24 24"><path d="M6.6 10.8a15 15 0 006.6 6.6l2.2-2.2a1 1 0 011-.25 11 11 0 003.6.6 1 1 0 011 1V20a1 1 0 01-1 1A17 17 0 013 4a1 1 0 011-1h3.5a1 1 0 011 1 11 11 0 00.6 3.6 1 1 0 01-.25 1z" fill="#5ec4cf"/></svg>
      555-014-2730
    </div>
    <div class="footer-contact">
      <div class="footer-email">info@solenne-care.ca <span class="dot"></span></div>
      <div class="footer-web">www.solenne-care.ca <span class="dot"></span></div>
    </div>
  </footer>
</section>

<!-- Brain health flyer -->
<section class="flyer flyer--brain">
  <div class="abs info-band">Velmora Wellness Center is a non-profit organization stemming from the merger of NVBIS (Northern Valley Brain Injury Society) and EFBIRS (Eastfield Brain Injury Relearning Society). Velmora Wellness Center offers programs and services at no cost to adults who have sustained an acquired brain injury, and their families. Services are offered from offices in Cedarford and Linmouth.</div>
  <div class="abs call-bar">
    <span class="call-script">Call Us</span>
    <svg width="20" height="20" viewBox="0 0 24 24"><path d="M6.6 10.8a15 15 0 006.6 6.6l2.2-2.2a1 1 0 011-.25 11 11 0 003.6.6 1 1 0 011 1V20a1 1 0 01-1 1A17 17 0 013 4a1 1 0 011-1h3.5a1 1 0 011 1 11 11 0 00.6 3.6 1 1 0 01-.25 1z" fill="#5ec4cf"/></svg>
    <span class="call-num">555-014-2730</span>
  </div>
  <div class="abs partner-corner">
    <span class="partner-mark"></span>
    <div class="partner-name">Velmora Wellness Center</div>
  </div>

  <div class="abs brain-badge badge-left" role="img" aria-label="Icon of a healthy brain"><span></span></div>
  <h2 class="abs brain-title">Keeping Your Brain <em>Healthy</em></h2>
  <div class="abs brain-badge badge-right" role="img" aria-label="Icon of a brain struck by lightning"><span></span></div>

  <svg class="abs arrows" width="520" height="738" viewBox="0 0 520 738">
    <path d="M129 240L250 327H215V652a14 14 0 01-14 14H54a14 14 0 01-14-14V327H11z" fill="#5ec4cf"/>
    <path d="M295 265a16 16 0 0116-16h148a16 16 0 0116 16V586h31L385 668 266 586h29z" fill="#1b1b1b"/>
  </svg>

  <h3 class="abs list-title boosters-title">BRAIN<br>BOOSTERS</h3>
  <ul class="abs food-list boosters">
    <li><i></i><div><strong>OPT FOR WHOLEGRAINS</strong><span>The brain needs energy</span></div></li>
    <li><i></i><div><strong>EAT OILY FISH</strong><span>Essential fatty acids can't be made by the body</span></div></li>
    <li><i></i><div><strong>BINGE ON BLUEBERRIES</strong><span>Effective in delaying short term memory loss</span></div></li>
    <li><i></i><div><strong>EAT MORE TOMATOES</strong><span>Protect against free radical damage linked to dementia</span></div></li>
    <li><i></i><div><strong>ADD VITALITY WITH VITAMINS</strong><span>B6, B12 &amp; folic acid reduce homocysteine in the blood</span></div></li>
    <li><i></i><div><strong>GET A BLACKCURRANT BOOST</strong><span>Increase mental agility</span></div></li>
    <li><i></i><div><strong>PICK UP ON PUMPKIN SEEDS</strong><span>(Zinc) Enhancing memory and thinking skills</span></div></li>
    <li><i></i><div><strong>BET ON BROCCOLI</strong><span>(Vit K) Enhance cognitive function &amp; improve brain power</span></div></li>
    <li><i></i><div><strong>GO NUTS</strong><span>(Vit E) Prevent cognitive decline</span></div></li>
  </ul>

  <h3 class="abs list-title busters-title">BRAIN<br>BUSTERS</h3>
  <ul class="abs food-list busters">
    <li><i></i><div><strong>FATTY FAST FOODS</strong><span>Connected with brain shrinkage that can lead to Alzheimer's</span></div></li>
    <li><i></i><div><strong>SALTY FOODS</strong><span>They are hard on the brain</span></div></li>
    <li><i></i><div><strong>PROCESSED FOODS</strong><span>Artificial additives affect cognitive functioning of some children</span></div></li>
    <li><i></i><div><strong>FRIED FOODS</strong><span>Raised risk of neurologic diseases like Alzheimer's &amp; Parkinson's</span></div></li>
    <li><i></i><div><strong>FOODS W/ PESTICIDE RESIDUE</strong><span>Affect children's IQ &amp; on preterm birth &amp; ADHD</span></div></li>
    <li><i></i><div><strong>SLEEP AIDS PM</strong><span>Cloud your brain</span></div></li>
    <li><i></i><div><strong>ALCOHOL</strong><span>In excess will cloud your memory</span></div></li>
    <li><i></i><div><strong>ARTIFICIAL SWEETENERS</strong><span>Bad for memory</span></div></li>
    <li><i></i><div><strong>JUNK FOOD</strong><span>Bad for brain</span></div></li>
  </ul>

  <footer class="abs footer">
    <svg class="footer-swoosh" width="300" height="76" viewBox="0 0 300 76"><path d="M0 76C80 30 170 8 300 0v76z" fill="#5ec4cf"/><path d="M40 76C110 42 190 26 300 22v54z" fill="#5ec4cf"/></svg>
    <div class="footer-brand">
      <div class="n">SOLENNE</div>
      <div class="s">HEALTHCARE</div>
    </div>
    <div class="footer-contact">
      <div class="footer-email">info@solenne-care.ca <span class="dot"></span></div>
      <div class="footer-web">www.solenne-care.ca <span class="dot"></span></div>
    </div>
  </footer>
</section>

</body>
</html>
```